7QK Pop Up Shop Clearance Flyer

We sell furniture. We opened up recently a temporary pop up shop to clear some stock we had from our old shop. So we don't have a full collection just our clearance lines that we want to get rid of - but the customer doesn't need to know this! Therefore the aim of this leaflet is to attract customers and make them come in - once they are there they might see something they like. As we will not be there for long - just a few more weeks.
We need a flyer to promote locally our pop up shop (temporary shop) with a Clearance Sale. The flyer will be sent by post or by hand to the local residents and by email to ex customers that bought from us before and we have their email address...
We need a modern fresh design flyer. At the next stage we will provide text for each item (brief description, dimensions and price) so allow some space for this.
Maybe we need to add a message or something to make people want to come quickly? For example most of the items are ex display or the last item and if they want it they should hurry as one is gone its gone. or you may have a better suggestion - let me know.
if you want to see some ideas of our website then 7QK.co.uk

Target Market(s)

Local Residents around shop

Industry/Entity Type

Retail

Colors
0255a3
3176b5
85abd2

Requirements
Must have
• price tag showing RRP or WAS price and the Clearance Sale price
• Opening Hours: Mon-Fri 9:00am - 5:00pm, Sat: 9:00am - 4:00pm, Sun: Closed
• Tel: 0208 915 2730
• Shop Address: 184 Birch Rowe, Elmwick Vale, London, N21 7PD
Nice to have
• Parking behind Bo Tarvins
• Map of location

```html
<!DOCTYPE html>
<html lang="en">
<head>
<meta charset="utf-8">
<title>7QK Furniture – Clearance Flyer</title>
<link rel="stylesheet" href="https://fonts.googleapis.com/css2?family=Varela+Round&family=Roboto+Condensed:wght@300;400&family=Lato:wght@400;700&display=swap">
<style>
:root{
  --blue-deep:#0255a3;
  --blue-mid:#3176b5;
  --blue-soft:#85abd2;
  --navy:#1a2a4a;
  --ink:#222428;
  --paper:#ffffff;
  --stage:#9a9a9a;
  --tag-red:#d0202a;
}
*{box-sizing:border-box;margin:0;padding:0}
html,body{width:960px;height:1200px;overflow:hidden}
body{background:var(--stage);font-family:"Lato",sans-serif;position:relative}
.flyer{position:absolute;top:250px;width:450px;height:636px;overflow:hidden;background:var(--paper);box-shadow:0 6px 18px rgba(0,0,0,.35)}
.flyer--front{left:20px}
.flyer--back{left:490px}
.side-label{position:absolute;top:912px;width:450px;text-align:center;font-size:30px;color:#111}
.side-label--front{left:20px}
.side-label--back{left:490px}

/* front */
.photo{position:absolute}
.photo--living{left:0;top:0;width:450px;height:343px;
  background:
    radial-gradient(ellipse 150px 60px at 240px 205px,#3c4250 0%,#3c4250 55%,rgba(60,66,80,0) 100%),
    radial-gradient(ellipse 50px 60px at 375px 230px,#2f6fa8 0%,rgba(47,111,168,0) 100%),
    linear-gradient(90deg,rgba(255,255,255,0) 0%,rgba(255,255,255,.5) 70%,rgba(255,255,255,0) 100%),
    linear-gradient(180deg,#eef1f3 0%,#e2e6ea 45%,#d4d8dc 62%,#e9eaeb 100%)}
.photo--bedroom{left:0;top:352px;width:450px;height:183px;
  background:
    radial-gradient(ellipse 140px 50px at 330px 120px,#2c4c7c 0%,rgba(44,76,124,0) 100%),
    linear-gradient(160deg,#4f79ad 0%,#6e8fb9 50%,#3f5f8e 100%)}
.photo--map{left:293px;top:544px;width:157px;height:92px;
  background:radial-gradient(circle at 78px 46px,#c9c9c9 0%,#e6e6e6 40%,#f0f0f0 100%)}
.overlay{position:absolute;left:0;top:0}
.brand-front{position:absolute;left:160px;top:20px;width:150px;text-align:center}
.brand-front__mark{font-family:"Roboto Condensed",sans-serif;font-weight:400;font-size:62px;line-height:1;color:var(--navy)}
.brand-front__name{font-family:"Roboto Condensed",sans-serif;font-weight:300;font-size:13px;margin-top:16px;color:var(--navy)}
.brand-front__tag{font-family:"Roboto Condensed",sans-serif;font-weight:300;font-size:7px;color:var(--navy)}
.headline{position:absolute;left:24px;top:220px;color:var(--paper);font-family:"Varela Round",sans-serif}
.headline__big{font-size:38px;line-height:1;letter-spacing:.5px}
.headline__small{font-size:21px;margin:6px 0 4px}
.hours{position:absolute;left:16px;top:376px;color:var(--paper);font-family:"Varela Round",sans-serif;font-size:13px}
.hours__title{font-size:14px;margin-bottom:16px}
.hours__row{line-height:19px}
.contact{position:absolute;left:16px;color:var(--paper);font-family:"Varela Round",sans-serif;font-size:12px;display:flex;align-items:center;gap:9px}
.contact--phone{top:486px}
.contact--web{top:509px}
.social{position:absolute;top:497px;width:20px;height:20px;border:1.5px solid var(--paper);border-radius:50%}
.social--one{left:179px}
.social--two{left:209px}
.address-bar{position:absolute;left:0;top:544px;width:293px;height:38px;background:var(--blue-mid);color:var(--paper);font-family:"Varela Round",sans-serif;font-size:11px;display:flex;align-items:center;gap:8px;padding-left:16px;white-space:nowrap}
.parking{position:absolute;left:15px;top:600px;color:var(--blue-deep);font-family:"Varela Round",sans-serif;font-size:13px}
.bottom-strip{position:absolute;left:0;top:627px;width:293px;height:9px;background:var(--blue-mid)}

/* back */
.back-header{position:absolute;left:0;top:0;width:450px;height:76px;background:var(--paper);display:flex;align-items:center;justify-content:center;gap:14px}
.back-header__mark{font-family:"Roboto Condensed",sans-serif;font-weight:400;font-size:40px;color:var(--navy)}
.back-header__name{font-family:"Roboto Condensed",sans-serif;font-weight:300;font-size:25px;color:var(--ink);line-height:1}
.back-header__tag{font-family:"Roboto Condensed",sans-serif;font-weight:300;font-size:13px;color:var(--ink);margin-top:2px;padding-left:18px}
.back-body{position:absolute;left:0;top:76px;width:450px;height:560px;background:var(--blue-deep)}
.product-grid{position:absolute;left:26px;top:12px;display:grid;grid-template-columns:repeat(3,118px);column-gap:21px;row-gap:15px}
.product{width:118px;height:120px}
.price-tag{position:relative;height:11px;background:var(--ink);color:var(--paper);font-size:5.5px;font-weight:400;display:flex;align-items:center;gap:6px;padding-left:14px;white-space:nowrap}
.price-tag::before{content:"";position:absolute;left:0;top:0;width:6px;height:14px;background:var(--tag-red)}
.price-tag b{font-weight:700}
.product__photo{--tone:#8a8f96;height:89px;
  background:
    radial-gradient(ellipse 46px 26px at 59px 50px,var(--tone) 0%,var(--tone) 45%,rgba(255,255,255,0) 100%),
    linear-gradient(180deg,#ffffff,#f1f1f1)}
.product__photo--grey{--tone:#5e6168}
.product__photo--brown{--tone:#7a5a44}
.product__photo--green{--tone:#0f8a76}
.product__photo--black{--tone:#2a2b2e}
.product__photo--slate{--tone:#6f7682}
.product__photo--white{--tone:#d7d8da}
.product__photo--glass{--tone:#cfd8dc}
.product__photo--wood{--tone:#b5763a}
.product__photo--taupe{--tone:#7d786f}
.product__text{color:var(--paper);font-size:6.5px;font-weight:400;line-height:8px;padding:8px 0 0 5px}
</style>
</head>
<body>

<section class="flyer flyer--front" aria-label="Flyer front side">
  <div class="photo photo--living" role="img" aria-label="Photo of a grey tufted sofa with a blue throw in a bright living room"></div>
  <svg class="overlay" width="450" height="636" viewBox="0 0 450 636" aria-hidden="true">
    <polygon points="0,0 70,0 0,60" fill="#3176b5" opacity=".85"/>
    <polygon points="0,110 0,343 330,343" fill="#0255a3" opacity=".85"/>
    <polygon points="90,140 0,343 330,343" fill="#3176b5" opacity=".55"/>
    <polygon points="160,0 310,0 310,145 160,145" fill="#b9cbe6" opacity=".75"/>
    <polygon points="355,0 450,0 450,110" fill="#2a2d33" opacity=".75"/>
  </svg>
  <div class="brand-front">
    <div class="brand-front__mark">7QK</div>
    <div class="brand-front__name">7QK FURNITURE</div>
    <div class="brand-front__tag">TRADE FURNITURE SOLUTIONS</div>
  </div>
  <div class="headline">
    <div class="headline__big">QUALITY</div>
    <div class="headline__small">Doesn’t have to be</div>
    <div class="headline__big">EXPENSIVE</div>
  </div>

  <div class="photo photo--bedroom" role="img" aria-label="Photo of a bedroom with a wooden bed, tinted blue"></div>
  <svg class="overlay" style="top:352px" width="450" height="183" viewBox="0 0 450 183" aria-hidden="true">
    <polygon points="0,0 128,0 312,183 0,183" fill="#22252a" opacity=".92"/>
    <polygon points="128,0 150,0 334,183 312,183" fill="#0255a3" opacity=".8"/>
  </svg>
  <div class="hours">
    <div class="hours__title">Opening Hours</div>
    <div class="hours__row">Mon-Fri:&nbsp; 9:00am - 5:00pm</div>
    <div class="hours__row">Sat:&nbsp; 9:00am - 4:00pm</div>
    <div class="hours__row">Sun:&nbsp; Closed</div>
  </div>
  <div class="contact contact--phone">
    <svg width="12" height="12" viewBox="0 0 12 12" aria-hidden="true"><circle cx="6" cy="6" r="5.3" fill="none" stroke="#fff" stroke-width="1"/><path d="M4 3.2 L5 4.6 L4.5 5.3 Q5.3 6.8 6.7 7.5 L7.4 7 L8.8 8 L8.2 8.9 Q5 8.6 3.2 4 Z" fill="#fff"/></svg>
    <span>0208 915 2730</span>
  </div>
  <div class="contact contact--web">
    <svg width="12" height="12" viewBox="0 0 12 12" aria-hidden="true"><circle cx="6" cy="6" r="5.3" fill="none" stroke="#fff" stroke-width="1"/><ellipse cx="6" cy="6" rx="2.3" ry="5.3" fill="none" stroke="#fff" stroke-width=".8"/><line x1=".7" y1="6" x2="11.3" y2="6" stroke="#fff" stroke-width=".8"/></svg>
    <span>www.7QK.co.uk</span>
  </div>
  <span class="social social--one" aria-hidden="true"></span>
  <span class="social social--two" aria-hidden="true"></span>

  <div class="address-bar">
    <svg width="10" height="12" viewBox="0 0 10 12" aria-hidden="true"><path d="M5 11.5 C2 8 1 6.3 1 4.5 A4 4 0 0 1 9 4.5 C9 6.3 8 8 5 11.5 Z" fill="none" stroke="#fff" stroke-width="1"/><circle cx="5" cy="4.5" r="1.4" fill="#fff"/></svg>
    <span>184 Birch Rowe, Elmwick Vale, London, N21 7PD</span>
  </div>
  <div class="parking">Parking behind Bo Tarvins</div>
  <div class="bottom-strip"></div>
  <div class="photo photo--map" role="img" aria-label="Street map showing the shop location"></div>
</section>

<section class="flyer flyer--back" aria-label="Flyer back side">
  <header class="back-header">
    <span class="back-header__mark">7QK</span>
    <div>
      <div class="back-header__name">7QK FURNITURE</div>
      <div class="back-header__tag">TRADE FURNITURE SOLUTIONS</div>
    </div>
  </header>
  <div class="back-body">
    <svg class="overlay" width="450" height="560" viewBox="0 0 450 560" aria-hidden="true">
      <polygon points="0,0 130,0 0,260" fill="#1a4a8c" opacity=".6"/>
      <polygon points="450,180 450,560 170,560" fill="#3176b5" opacity=".5"/>
      <polygon points="0,330 0,560 120,560" fill="#1a4a8c" opacity=".5"/>
    </svg>
    <div class="product-grid">
      <article class="product"><div class="price-tag"><span>RRP Price <b>$ 000</b></span><span>Sale Price <b>$ 000</b></span></div><div class="product__photo product__photo--grey" role="img" aria-label="Grey corner sofa"></div><p class="product__text">Lorem ipsum dolor sit amet,<br>consectetur adipiscing elit</p></article>
      <article class="product"><div class="price-tag"><span>RRP Price <b>$ 000</b></span><span>Sale Price <b>$ 000</b></span></div><div class="product__photo product__photo--brown" role="img" aria-label="Brown corner sofa with patterned cushions"></div><p class="product__text">Lorem ipsum dolor sit amet,<br>consectetur adipiscing elit</p></article>
      <article class="product"><div class="price-tag"><span>RRP Price <b>$ 000</b></span><span>Sale Price <b>$ 000</b></span></div><div class="product__photo product__photo--green" role="img" aria-label="Green sofa bed"></div><p class="product__text">Lorem ipsum dolor sit amet,<br>consectetur adipiscing elit</p></article>
      <article class="product"><div class="price-tag"><span>RRP Price <b>$ 000</b></span><span>Sale Price <b>$ 000</b></span></div><div class="product__photo product__photo--black" role="img" aria-label="Black two-seat sofa"></div><p class="product__text">Lorem ipsum dolor sit amet,<br>consectetur adipiscing elit</p></article>
      <article class="product"><div class="price-tag"><span>RRP Price <b>$ 000</b></span><span>Sale Price <b>$ 000</b></span></div><div class="product__photo product__photo--slate" role="img" aria-label="Grey fabric sofa bed"></div><p class="product__text">Lorem ipsum dolor sit amet,<br>consectetur adipiscing elit</p></article>
      <article class="product"><div class="price-tag"><span>RRP Price <b>$ 000</b></span><span>Sale Price <b>$ 000</b></span></div><div class="product__photo product__photo--white" role="img" aria-label="White desk with drawers"></div><p class="product__text">Lorem ipsum dolor sit amet,<br>consectetur adipiscing elit</p></article>
      <article class="product"><div class="price-tag"><span>RRP Price <b>$ 000</b></span><span>Sale Price <b>$ 000</b></span></div><div class="product__photo product__photo--glass" role="img" aria-label="Glass and chrome coffee table"></div><p class="product__text">Lorem ipsum dolor sit amet,<br>consectetur adipiscing elit</p></article>
      <article class="product"><div class="price-tag"><span>RRP Price <b>$ 000</b></span><span>Sale Price <b>$ 000</b></span></div><div class="product__photo product__photo--slate" role="img" aria-label="Grey corner sofa bed"></div><p class="product__text">Lorem ipsum dolor sit amet,<br>consectetur adipiscing elit</p></article>
      <article class="product"><div class="price-tag"><span>RRP Price <b>$ 000</b></span><span>Sale Price <b>$ 000</b></span></div><div class="product__photo product__photo--wood" role="img" aria-label="Wooden dining table with two chairs"></div><p class="product__text">Lorem ipsum dolor sit amet,<br>consectetur adipiscing elit</p></article>
      <article class="product"><div class="price-tag"><span>RRP Price <b>$ 000</b></span><span>Sale Price <b>$ 000</b></span></div><div class="product__photo product__photo--taupe" role="img" aria-label="Grey upholstered dining chair"></div><p class="product__text">Lorem ipsum dolor sit amet,<br>consectetur adipiscing elit</p></article>
      <article class="product"><div class="price-tag"><span>RRP Price <b>$ 000</b></span><span>Sale Price <b>$ 000</b></span></div><div class="product__photo product__photo--black" role="img" aria-label="Black dining chair with chrome legs"></div><p class="product__text">Lorem ipsum dolor sit amet,<br>consectetur adipiscing elit</p></article>
      <article class="product"><div class="price-tag"><span>RRP Price <b>$ 000</b></span><span>Sale Price <b>$ 000</b></span></div><div class="product__photo product__photo--glass" role="img" aria-label="White glass dining table with chrome legs"></div><p class="product__text">Lorem ipsum dolor sit amet,<br>consectetur adipiscing elit</p></article>
    </div>
  </div>
</section>

<div class="side-label side-label--front">Front side</div>
<div class="side-label side-label--back">Back side</div>

</body>
</html>
```